PowerPoint Design Project

Lanterfield Estate Partners is a Melbourne based property development management company. We provide a comprehensive range of development management services to a select group of listed developers, private landowners, overseas investors and development partners and institutional clients. Our website provides additional information about the company:
http://www.lanterfieldep.example.au
We are looking for a versatile powerpoint design that can be used across a wide variety of presentations including; pitch documents, client reports, Information memorandums, and downloadable credential packs etc. We have attached a good example document.
Updates

Industry/Entity Type

It Company

Requirements
Must have
• The design should have the following slides as a minimum: Intro Page, transition slides, profile slides, slides for graphics,

```html
<!DOCTYPE html>
<html lang="en">
<head>
<meta charset="utf-8">
<title>Lanterfield Estate Partners – Presentation Template</title>
<link href="https://fonts.googleapis.com/css2?family=PT+Sans:ital,wght@0,400;0,700;1,700&display=swap" rel="stylesheet">
<style>
:root{
  --backdrop:#e6e3de;
  --slide:#ffffff;
  --header:#48474c;
  --ink:#1a1a1a;
  --body:#6f6f6f;
  --footer-grey:#a3a3a5;
  --footer-black:#0d0d0d;
  --rule:#3a5a9a;
  --cyl-top:#111;
}
*{box-sizing:border-box;margin:0;padding:0}
html,body{width:1200px;height:442px;overflow:hidden}
body{background:var(--backdrop);font-family:"PT Sans",Arial,sans-serif;color:var(--ink);position:relative}
.slide{position:absolute;width:265px;height:198px;background:var(--slide);overflow:hidden;box-shadow:0 1px 3px rgba(0,0,0,.18)}
.col-1{left:26px}.col-2{left:324px}.col-3{left:612px}.col-4{left:897px}
.row-1{top:13px}.row-2{top:229px}
.slide-header{position:absolute;left:0;top:0;width:100%;height:18px;background:var(--header);color:#fff;font-size:11.5px;font-weight:400;line-height:18px;padding-left:13px;text-transform:uppercase;letter-spacing:.2px;z-index:2}
.slide-footer{position:absolute;left:0;bottom:0;width:100%;height:8px;background:var(--footer-grey)}
.slide-footer .url{position:absolute;right:0;top:0;width:122px;height:8px;background:var(--footer-black);color:#fff;font-size:5px;line-height:8px;letter-spacing:.9px;text-align:center}
.slide-footer .page{position:absolute;left:125px;top:0;width:12px;height:8px;border-radius:6px 6px 0 0;background:#fff;font-size:4px;line-height:9px;text-align:center;color:#333}
.copy{font-size:5.2px;line-height:7.6px;color:var(--body)}
.photo{position:absolute}
.brand{position:absolute;left:0;width:100%;text-align:center;font-weight:700;font-size:13px;letter-spacing:.4px;color:var(--ink);text-transform:uppercase}
.brand::before{content:"";display:inline-block;width:8px;height:8px;background:var(--ink);margin-right:5px;vertical-align:0}
.cover .brand{top:80px}
.cover-title{position:absolute;top:130px;left:0;width:100%;text-align:center;font-size:15px;font-weight:400;font-family:Arial,"PT Sans",sans-serif}
.intro .copy{position:absolute;left:13px;right:13px;top:26px}
.intro .copy p+p{margin-top:3px}
.intro .ph-a{left:0;top:98px;width:131px;height:74px;background:linear-gradient(180deg,#6f8fbf,#3b4d6e 70%,#2b2f3b)}
.intro .ph-b{left:134px;top:98px;width:131px;height:74px;background:linear-gradient(120deg,#d9d2cb,#b0362f 45%,#e8e2dc)}
.intro .blue-rule{position:absolute;left:0;top:172px;width:100%;height:2px;background:var(--rule)}
.graphics svg{position:absolute;left:0;top:18px}
.table .bg{left:0;top:18px;width:100%;height:172px;background:linear-gradient(90deg,#f1f1f3,#e7e6eb 60%,#d9d8de);opacity:.9}
.table .cell{position:absolute;width:118px;font-size:6.6px;line-height:8px;color:#555}
.table .cell-title{font-size:6.6px;font-weight:400;color:#333}
.transition .strip{position:absolute;left:0;top:20px;width:100%;height:84px;border-top:1px solid var(--rule);border-bottom:1px solid var(--rule)}
.transition .ph-a{left:0;top:0;width:150px;height:82px;background:linear-gradient(180deg,#f2f1ef,#d8d6d2);clip-path:polygon(0 0,100% 0,86% 100%,0 100%)}
.transition .ph-b{left:129px;top:0;width:136px;height:82px;background:linear-gradient(135deg,#6e5aa8,#2f2a4a 60%,#8a6c3c);clip-path:polygon(16% 0,100% 0,100% 100%,0 100%)}
.transition .part-title{position:absolute;top:111px;left:0;width:100%;text-align:center;font-size:14px;line-height:18px;font-weight:700}
.transition .copy{position:absolute;top:132px;left:46px;right:46px;text-align:center}
.profile .ph{left:13px;top:57px;width:120px;height:92px;background:linear-gradient(180deg,#f4f4f4,#cfc9c3 55%,#2d2d33);border:1px solid #bbb}
.profile .copy{position:absolute;left:148px;right:13px;top:52px;text-align:justify}
.lorem .copy{position:absolute;left:28px;right:28px;top:30px}
.lorem .ph-a{left:28px;top:78px;width:110px;height:96px;background:linear-gradient(180deg,#c8302a 0 22%,#eae5df 22%,#bfa48e);border:1px solid #bbb}
.lorem .ph-b{left:142px;top:78px;width:96px;height:96px;background:linear-gradient(160deg,#f3efe9,#d7b9a0 60%,#7fa6c4);border:1px solid #bbb}
.closing .brand{top:54px}
.closing .thanks{position:absolute;top:96px;left:0;width:100%;text-align:center;font-size:13.5px;line-height:15.5px;font-style:italic;font-weight:700;font-family:Arial,"PT Sans",sans-serif}
.closing .contact{position:absolute;top:163px;left:0;width:100%;text-align:center;font-size:5.4px;line-height:9px;color:#333}
.closing .contact b{font-style:italic}
</style>
</head>
<body>

<section class="slide cover col-1 row-1">
  <div class="brand">Lanterfield Estate Partners</div>
  <h1 class="cover-title">Title of Presentation</h1>
  <div class="slide-footer"><span class="page">1</span><span class="url">www.lanterfieldep.example.au</span></div>
</section>

<section class="slide intro col-2 row-1">
  <h2 class="slide-header">Intro Page</h2>
  <div class="copy">
    <p>Lorem ipsum d olor sit amet, consectetuer adipiscing elit, sed diam nonummy nibh euismod tincidunt ut laoreet dolore magna aliquam erat volutpat. Ut wisi enim ad minim veniam, quis nostrud exerci tation ullamcorper suscipit lobortis nisl ut aliquip ex ea commodo consequat. Duis autem vel eum iriure dolor in hendrerit in vulputate velit esse molestie consequat, vel illum dolore eu feugiat nulla facilisis.</p>
    <p>Lorem ipsum d olor sit amet, consectetuer adipiscing elit, sed diam nonummy nibh euismod tincidunt ut laoreet dolore magnae consequat, vel illum dolore eu feugiat nulla facilisis.</p>
  </div>
  <div class="photo ph-a" role="img" aria-label="Photo of flags in front of a modern office building under a blue sky"></div>
  <div class="photo ph-b" role="img" aria-label="Photo of a red staircase in a bright interior"></div>
  <div class="blue-rule"></div>
  <div class="slide-footer"><span class="page">2</span><span class="url">www.lanterfieldep.example.au</span></div>
</section>

<section class="slide graphics col-3 row-1">
  <h2 class="slide-header">Slides for Graphics</h2>
  <svg width="265" height="172" viewBox="0 0 265 172" aria-label="Diagram of four labelled columns of data stores">
    <defs>
      <linearGradient id="cylSide" x1="0" x2="1">
        <stop offset="0" stop-color="#7c7c7c"/><stop offset=".45" stop-color="#d2d2d2"/><stop offset="1" stop-color="#858585"/>
      </linearGradient>
      <g id="cyl">
        <rect x="-17" y="0" width="34" height="24" fill="url(#cylSide)"/>
        <ellipse cx="0" cy="24" rx="17" ry="4" fill="#8a8a8a"/>
        <ellipse cx="0" cy="0" rx="17" ry="4" fill="var(--cyl-top)"/>
        <text x="0" y="15" font-size="4.6" fill="#fff" text-anchor="middle" font-family="PT Sans, sans-serif" font-weight="700">Lorem</text>
      </g>
    </defs>
    <g stroke="#bbb" stroke-width=".7" fill="none">
      <path d="M34 53 H26 V86 H34 M32 98 H34"/>
      <path d="M50 53 H116 M50 86 H116 M50 119 H116"/>
      <path d="M150 53 H166 M150 86 H166 M150 119 H166 M200 53 H216 M200 86 H216 M200 119 H216"/>
    </g>
    <g font-family="PT Sans, sans-serif" font-size="5.2" font-weight="700" fill="#fff" text-anchor="middle">
      <rect x="39" y="42" width="41" height="17" rx="2" fill="#000"/><text x="59.5" y="53">Lorem ipsum</text>
      <rect x="90" y="42" width="41" height="17" rx="2" fill="#000"/><text x="110.5" y="53">Lorem ipsum</text>
      <rect x="140" y="42" width="41" height="17" rx="2" fill="#000"/><text x="160.5" y="53">Lorem ipsum</text>
      <rect x="191" y="42" width="41" height="17" rx="2" fill="#000"/><text x="211.5" y="53">Lorem ipsum</text>
    </g>
    <use href="#cyl" x="59" y="69"/><use href="#cyl" x="59" y="102"/>
    <use href="#cyl" x="110" y="69"/><use href="#cyl" x="110" y="102"/><use href="#cyl" x="110" y="135"/>
    <use href="#cyl" x="160" y="69"/><use href="#cyl" x="160" y="102"/><use href="#cyl" x="160" y="135"/>
    <use href="#cyl" x="211" y="69"/><use href="#cyl" x="211" y="102"/><use href="#cyl" x="211" y="135"/>
  </svg>
  <div class="slide-footer"><span class="page">3</span><span class="url">www.lanterfieldep.example.au</span></div>
</section>

<section class="slide table col-4 row-1">
  <h2 class="slide-header">Slides for Table</h2>
  <div class="photo bg" role="img" aria-label="Faint photo of a building interior as a background"></div>
  <div class="cell" style="left:12px;top:43px"><h3 class="cell-title">Sub Title-1</h3>Lorem ipsum dolor sit amet, etuer.Lorem ipsum dolor sit amet, etuer.Lorem ipsum dolor sit amet, etuer.Lorem ipsum dolor</div>
  <div class="cell" style="left:142px;top:43px"><h3 class="cell-title">Sub Title-1</h3>Lorem ipsum dolor sit amet, etuer.Lorem ipsum dolor sit amet, etuer.Lorem ipsum dolor sit amet, etuer.Lorem ipsum dolor</div>
  <div class="cell" style="left:12px;top:90px"><h3 class="cell-title">Sub Title-2</h3>Lorem ipsum dolor sit amet, etuer.Lorem ipsum dolor sit amet, etuer.Lorem ipsum dolor sit amet, etuer.Lorem ipsum dolor</div>
  <div class="cell" style="left:142px;top:90px"><h3 class="cell-title">Sub Title-2</h3>Lorem ipsum dolor sit amet, etuer.Lorem ipsum dolor sit amet, etuer.Lorem ipsum dolor sit amet, etuer.Lorem ipsum dolor</div>
  <div class="cell" style="left:12px;top:137px"><h3 class="cell-title">Sub Title-3</h3>Lorem ipsum dolor sit amet, etuer.Lorem ipsum dolor sit amet, etuer.Lorem ipsum dolor sit amet, etuer.Lorem ipsum dolor</div>
  <div class="cell" style="left:142px;top:137px"><h3 class="cell-title">Sub Title-3</h3>Lorem ipsum dolor sit amet, etuer.Lorem ipsum dolor sit amet, etuer.Lorem ipsum dolor sit amet, etuer.Lorem ipsum dolor</div>
  <div class="slide-footer"><span class="page">4</span><span class="url">www.lanterfieldep.example.au</span></div>
</section>

<section class="slide transition col-1 row-2">
  <h2 class="slide-header">Transition Slides</h2>
  <div class="strip">
    <div class="photo ph-a" role="img" aria-label="Photo of a bright white living room interior"></div>
    <div class="photo ph-b" role="img" aria-label="Photo of a building facade lit at dusk"></div>
  </div>
  <h3 class="part-title">PART 3</h3>
  <p class="copy">Orem ipsum dolor sit amet, consectetuer adipiscing elit, sed diam nonummy nibh euismod tincidunt ut laoreet dolore magna aliquam erat volutpat. Ut wisi enim ad minim veniam, quis nostrud exerci tation ullamcorper suscipit lobortis nisl ut aliquip ex ea commodo consequat. Duis autem vel eum iriure dolor in hendrerit in</p>
  <div class="slide-footer"><span class="page">5</span><span class="url">www.lanterfieldep.example.au</span></div>
</section>

<section class="slide profile col-2 row-2">
  <h2 class="slide-header">Profile Slides</h2>
  <div class="photo ph" role="img" aria-label="Photo of three smiling business people in suits"></div>
  <p class="copy">Lorem ipsum dolor sit amet, consectetuer adipiscing elit, sed diam nonummy nibh euismod tincidunt ut laoreet dolore magna aliquam erat volutpat. Ut wisi enim ad minim veniam, quis nostrud exerci tation ullamcorper suscipit lobortis nisl ut aliquip ex ea commodo consequat. Duis autem vel eum iri. Lorem ipsum dolor sit amet, consectetuer adipiscing elit, sed diam nonummy nibh euismod</p>
  <div class="slide-footer"><span class="page">6</span><span class="url">www.lanterfieldep.example.au</span></div>
</section>

<section class="slide lorem col-3 row-2">
  <h2 class="slide-header">Lorem Ipsum</h2>
  <p class="copy">Orem ipsum dolor sit amet, consectetuer adipiscing elit, sed diam nonummy nibh euismod tincidunt ut laoreet dolore magna aliquam erat volutpat. Ut wisi enim ad minim veniam, quis nostrud exerci tation ullamcorper suscipit lobortis nisl ut aliquip ex ea commodo consequat.</p>
  <div class="photo ph-a" role="img" aria-label="Photo of a family in front of a house with a red roof"></div>
  <div class="photo ph-b" role="img" aria-label="Photo of a smiling woman holding a card"></div>
  <div class="slide-footer"><span class="page">7</span><span class="url">www.lanterfieldep.example.au</span></div>
</section>

<section class="slide closing col-4 row-2">
  <div class="brand">Lanterfield Estate Partners</div>
  <p class="thanks">THANK YOU<br>FOR ATTENTION</p>
  <p class="contact"><b>phone:</b> 020 7946 0123 &nbsp;<b>Fax:</b> 020 7946 0124<br>14 Harrow Lane, London W1A 2ZZ</p>
  <div class="slide-footer"><span class="page">8</span><span class="url">www.lanterfieldep.example.au</span></div>
</section>

</body>
</html>
```